Digital Marketing Agency Landing Page

At VELMIT, we offer a comprehensive solution for solar companies' client acquisition needs in the rapidly growing industry. We handle end-to-end client acquisition, meaning we manage the entire lifecycle of capturing new clients—from initial lead generation to delivering the ready-to-buy homeowner. Our expertise in targeted advertising, data analytics, and customer relationship management ensures that we not only find potential customers but also nurture them through tailored engagement strategies until they are ready to make a purchase. By entrusting us with your client acquisition process, solar companies can focus on what they do best—providing sustainable energy solutions—while we work behind the scenes to grow your customer base and increase your market share.

We need to restructure our website to make it more professional. We don't need any complex functionalities. We are looking for someone that is good in design and can build a visually aesthetic website following our brand image. We only need a landing page and a lead form in the end. I would like to have only one page, but a relatively big one where people scroll down. I would like to have a minimal and classy look. Something that is timeless and elegant.

Structure:

initial page
About us
How we operate
Get in touch

Target Market(s)

Solar Comapanies

Industry/Entity Type

Marketing solautions

Coding

Coded - Design and coding required

Number of Pages Required

1 page

Requirements
Nice to have
• Inspirations: https://www.qz.lo/ https://www.junebrook.example/ https://www.megaroster.example/ https://pluno.example/

```html
<!DOCTYPE html>
<html lang="en">
<head>
<meta charset="utf-8">
<title>VELMIT — Client Acquisition for Solar Companies</title>
<link rel="stylesheet" href="https://fonts.googleapis.com/css2?family=Montserrat:wght@300&family=Open+Sans:wght@500;600&family=Roboto:wght@400;500&display=swap">
<style>
:root{
  --navy:#13202c;
  --navy-deep:#0e1f2d;
  --ink:#1b2733;
  --muted:#5d646b;
  --field:#ececec;
  --white:#ffffff;
  --line:#2a3540;
}
*{box-sizing:border-box;margin:0;padding:0}
html,body{width:1200px;height:2325px;overflow:hidden}
body{position:relative;background:var(--white);font-family:'Roboto',sans-serif;color:var(--ink)}

/* hero */
.hero{position:absolute;left:0;top:0;width:1200px;height:660px;
  background:linear-gradient(180deg,#1f2328 0%,rgba(31,35,40,.55) 18%,rgba(0,0,0,0) 32%),
  linear-gradient(100deg,#6f8794 0%,#9aa7ad 22%,#c7b1a4 45%,#a88a7a 62%,#4a3b36 80%,#2b2422 100%);}
.hero-photo{position:absolute;inset:0}
.brand{position:absolute;display:flex;align-items:center;gap:12px;font-family:'Montserrat',sans-serif;font-weight:300;font-size:32px;letter-spacing:1px;line-height:1}
.brand-mark{width:12px;height:12px;background:currentColor}
.hero .brand{left:110px;top:62px;color:var(--white)}
.nav{position:absolute;top:68px;font-size:16px;color:var(--white)}
.btn{position:absolute;display:flex;align-items:center;justify-content:center;font-weight:500;font-size:16px}
.btn::after{content:"";position:absolute;left:6px;top:6px;right:-6px;bottom:-6px;border:1px solid var(--line);z-index:-1}
.btn-light{background:var(--white);color:var(--ink)}
.btn-light::after{border-color:var(--white)}
.btn-dark{background:var(--navy);color:var(--white)}

.quote-frame{position:absolute;left:722px;top:191px;width:366px;height:413px;background:rgba(255,255,255,.38)}
.quote-card{position:absolute;left:748px;top:217px;width:314px;height:361px;background:var(--white)}
.quote-title{position:absolute;left:0;width:314px;top:32px;text-align:center;font-family:'Open Sans',sans-serif;font-weight:500;font-size:34px;color:var(--navy)}
.field{position:absolute;left:34px;width:246px;height:46px;background:var(--field);font-size:12px;color:#444;padding:17px 0 0 13px}
.quote-submit{position:absolute;left:34px;top:274px;width:246px;height:46px;background:var(--navy);color:var(--white);display:flex;align-items:center;justify-content:center;font-weight:500;font-size:15px}

/* how we operate */
.section-title{position:absolute;font-family:'Open Sans',sans-serif;font-weight:600;font-size:40px;color:var(--navy)}
.operate-intro{position:absolute;left:170px;width:860px;top:820px;text-align:center;font-size:16px;line-height:32px;color:var(--muted)}
.step-card{position:absolute;top:925px;width:307px;height:353px;background:var(--white);box-shadow:0 0 14px rgba(0,0,0,.06);text-align:center}
.step-card.featured{box-shadow:none;border:1px solid var(--line)}
.step-card.featured::after{content:"";position:absolute;left:8px;top:8px;right:-10px;bottom:-10px;border:1px solid var(--line)}
.step-icon{position:absolute;left:111px;top:42px;width:86px;height:86px;border-radius:50%;background:var(--navy)}
.step-title{position:absolute;left:0;right:0;top:150px;font-weight:500;font-size:19px;color:var(--ink)}
.step-body{position:absolute;left:36px;right:36px;top:186px;font-size:13.5px;line-height:23px;color:var(--muted)}
.step-link{position:absolute;left:0;right:0;top:295px;font-weight:500;font-size:14px;text-decoration:underline;color:var(--ink)}

/* about */
.about{position:absolute;left:0;top:1476px;width:1200px;height:573px;background:radial-gradient(circle at 70% 30%,#15293a 0%,var(--navy-deep) 60%)}
.about-photo{position:absolute;left:110px;top:72px;width:425px;height:439px;background:linear-gradient(135deg,#6e7e86 0%,#8c8477 45%,#4b4038 100%)}
.about-frame{position:absolute;left:118px;top:62px;width:427px;height:441px;border:1px solid rgba(255,255,255,.85)}
.about-title{color:var(--white);left:598px;top:70px}
.about-text{position:absolute;left:598px;top:146px;width:500px;font-size:14px;line-height:27.5px;color:var(--white)}
.about-text p+p{margin-top:27px}

/* footer */
.footer .brand{left:541px;top:2112px;color:var(--ink);gap:0}
.foot-link{position:absolute;top:2189px;font-size:16px;color:var(--muted)}
.social{position:absolute;top:2239px;width:26px;height:26px;border-radius:50%;background:var(--navy)}
.copyright{position:absolute;left:0;width:1200px;top:2297px;text-align:center;font-size:12.5px;color:var(--muted)}
</style>
</head>
<body>

<header class="hero">
  <div class="hero-photo" role="img" aria-label="Photo of two happy colleagues celebrating at an office desk"></div>
  <div class="brand"><span class="brand-mark"></span>VELMIT</div>
  <span class="nav" style="left:575px">Home</span>
  <span class="nav" style="left:677px">About Us</span>
  <span class="nav" style="left:801px">How We Operate</span>
  <a class="btn btn-light" style="left:965px;top:53px;width:122px;height:44px">Contact Us</a>

  <div class="quote-frame"></div>
  <form class="quote-card">
    <h2 class="quote-title">GET A QUOTE</h2>
    <div class="field" style="top:94px">Full Name *</div>
    <div class="field" style="top:154px">Email Address *</div>
    <div class="field" style="top:214px">Contact Number *</div>
    <div class="quote-submit">Request A Quote</div>
  </form>
</header>

<section class="operate">
  <h2 class="section-title" style="left:0;width:1200px;text-align:center;top:748px">HOW WE OPERATE</h2>
  <p class="operate-intro">We manage every step of winning new solar clients, from the first targeted ad to the final handover, so your sales team only speaks with homeowners who are informed, qualified and ready to buy.</p>

  <article class="step-card" style="left:99px">
    <div class="step-icon">
      <svg width="86" height="86" viewBox="0 0 86 86" fill="none" stroke="#fff" stroke-width="1.6">
        <rect x="25" y="33" width="36" height="24" rx="2"/><path d="M36 33v-4h14v4M25 43h36"/><rect x="40" y="40" width="6" height="6"/>
      </svg>
    </div>
    <h3 class="step-title">Lead Generation</h3>
    <p class="step-body">Targeted advertising campaigns reach homeowners in your service areas who are actively looking into solar for their homes.</p>
    <a class="step-link">View Details</a>
  </article>

  <article class="step-card featured" style="left:446px">
    <div class="step-icon">
      <svg width="86" height="86" viewBox="0 0 86 86" fill="none" stroke="#fff" stroke-width="1.6">
        <circle cx="43" cy="32" r="5"/><circle cx="33" cy="36" r="4"/><circle cx="53" cy="36" r="4"/>
        <path d="M26 50l8-6 9 5 9-5 8 6M34 44l9 9 9-9"/>
      </svg>
    </div>
    <h3 class="step-title">Tailored Nurturing</h3>
    <p class="step-body">Data analytics and tailored engagement keep every lead warm, answering questions until they feel confident about going solar.</p>
    <a class="step-link">View Details</a>
  </article>

  <article class="step-card" style="left:794px">
    <div class="step-icon">
      <svg width="86" height="86" viewBox="0 0 86 86" fill="none" stroke="#fff" stroke-width="1.6">
        <circle cx="48" cy="40" r="6"/><path d="M38 24v14M35 28l3-4 3 4M53 26h8v12h-8"/>
        <path d="M25 52l8-4h8l6 3h8l6-4M25 58l10-2 14 2 12-6"/>
      </svg>
    </div>
    <h3 class="step-title">Ready-to-Buy Delivery</h3>
    <p class="step-body">We hand your team qualified homeowners ready to purchase, so you grow your customer base and increase your market share.</p>
    <a class="step-link">View Details</a>
  </article>

  <a class="btn btn-dark" style="left:460px;top:1340px;width:120px;height:43px">View More</a>
  <a class="btn btn-dark" style="left:614px;top:1340px;width:120px;height:43px">Get Started</a>
</section>

<section class="about">
  <div class="about-photo" role="img" aria-label="Photo of three colleagues meeting around a laptop in a bright office"></div>
  <div class="about-frame"></div>
  <h2 class="section-title about-title">ABOUT US</h2>
  <div class="about-text">
    <p>VELMIT handles end-to-end client acquisition for solar companies in a rapidly growing industry. We manage the entire lifecycle of capturing new clients, from initial lead generation to delivering the ready-to-buy homeowner. Our expertise in targeted advertising, data analytics and relationship management means we find potential customers and nurture them until they buy.</p>
    <p>By entrusting us with your client acquisition, you focus on what you do best, providing sustainable energy solutions, while we work behind the scenes to grow your customer base.</p>
  </div>
  <a class="btn btn-light" style="left:597px;top:444px;width:122px;height:44px">Read More</a>
</section>

<footer class="footer">
  <div class="brand">VELMIT</div>
  <span class="foot-link" style="left:360px">Home</span>
  <span class="foot-link" style="left:463px">About Us</span>
  <span class="foot-link" style="left:587px">How We Operate</span>
  <span class="foot-link" style="left:749px">Contact Us</span>
  <span class="social" style="left:556px"></span>
  <span class="social" style="left:587px"></span>
  <span class="social" style="left:618px"></span>
  <p class="copyright">© Copyright 2023 | All Rights Reserved</p>
</footer>

</body>
</html>
```